Bref créative
Business Cards/Stationary Vandorik Law, P.C.
Professional
Colvin R. Vandorik
Attorney & Counselor at Law
489 Pellham Avenue
Worcester, Massachusetts 01604
Colvin@Vandorik-example.com
www.Vandorik-example.com
I would also like designs to include letterhead and envelopes. Thank you.
Would like to list the areas of practice on the back, Workers' Compensation, Car Accidents, Personal Injury, Family Law, Criminal Law

```html
<!DOCTYPE html>
<html lang="en">
<head>
<meta charset="utf-8">
<title>Vandorik Law, P.C. — Stationery</title>
<link rel="stylesheet" href="https://fonts.googleapis.com/css2?family=Open+Sans:wght@400;700&display=swap">
<style>
  :root {
    --navy: #1e3a8c;
    --navy-dark: #152c6e;
    --ink: #333a46;
    --muted: #6b7280;
    --paper: #ffffff;
    --backdrop: #e6e8ec;
  }
  * { box-sizing: border-box; margin: 0; padding: 0; }
  html, body { width: 1200px; height: 799px; overflow: hidden; }
  body {
    background: var(--backdrop);
    font-family: "Open Sans", Arial, sans-serif;
    color: var(--ink);
    position: relative;
  }
  .piece {
    position: absolute;
    background: var(--paper);
    box-shadow: 0 2px 10px rgba(0,0,0,.12);
    overflow: hidden;
  }
  .brand { display: flex; align-items: center; gap: 8px; }
  .brand-dot { border-radius: 50%; background: var(--navy); flex: none; }
  .brand-name { color: var(--navy); font-weight: 700; letter-spacing: .04em; white-space: nowrap; }

  /* Letterhead */
  .letterhead { left: 50px; top: 40px; width: 460px; height: 718px; padding: 36px 44px; }
  .letterhead .brand { justify-content: center; }
  .letterhead .brand-dot { width: 26px; height: 26px; }
  .letterhead .brand-name { font-size: 20px; }
  .letter-rule { height: 2px; background: var(--navy); margin: 12px 0 26px; }
  .letter-date { font-size: 9px; margin-bottom: 14px; }
  .recipient { font-size: 9px; line-height: 1.5; margin-bottom: 18px; }
  .letter-body p { font-size: 9px; line-height: 1.65; margin-bottom: 12px; }
  .closing { font-size: 9px; line-height: 1.5; margin-top: 20px; }
  .closing .signer { margin-top: 30px; font-weight: 700; }
  .letter-footer {
    position: absolute; left: 44px; right: 44px; bottom: 28px;
    border-top: 2px solid var(--navy); padding-top: 8px;
    font-size: 8px; color: var(--muted); text-align: center; letter-spacing: .02em;
  }

  /* Envelope front */
  .envelope-front { left: 550px; top: 40px; width: 600px; height: 262px; padding: 24px 28px; }
  .envelope-front .brand-dot { width: 22px; height: 22px; }
  .envelope-front .brand-name { font-size: 17px; }
  .return-address { font-size: 9px; color: var(--muted); margin-top: 8px; line-height: 1.5; padding-left: 30px; }
  .envelope-band { position: absolute; left: 0; right: 0; bottom: 0; height: 14px; background: var(--navy); }

  /* Envelope back */
  .envelope-back { left: 550px; top: 322px; width: 600px; height: 220px; }
  .envelope-back svg { display: block; }

  /* Business cards */
  .card { width: 290px; height: 170px; top: 570px; }
  .card-front { left: 550px; padding: 18px 20px; }
  .card-front .brand-dot { width: 16px; height: 16px; }
  .card-front .brand-name { font-size: 13px; }
  .contact-list { list-style: none; font-size: 8px; line-height: 1.65; margin-top: 12px; }
  .contact-list b { display: inline-block; width: 34px; color: var(--navy); }
  .card-holder { position: absolute; right: 20px; bottom: 18px; text-align: right; }
  .card-holder .name { font-size: 11px; font-weight: 700; color: var(--navy); }
  .card-holder .role { font-size: 8px; color: var(--muted); }
  .card-stripe { position: absolute; left: 0; right: 0; bottom: 0; height: 6px; background: var(--navy); }

  .card-back { left: 860px; background: var(--navy); color: #fff; padding: 20px; }
  .card-back .brand-dot { width: 16px; height: 16px; background: #fff; }
  .card-back .brand-name { font-size: 13px; color: #fff; }
  .practice-title { font-size: 8px; text-transform: uppercase; letter-spacing: .12em; margin: 16px 0 6px; opacity: .8; }
  .practice-list { list-style: none; font-size: 9px; line-height: 1.6; }
</style>
</head>
<body>

  <article class="piece letterhead">
    <div class="brand"><span class="brand-dot"></span><span class="brand-name">VANDORIK LAW, P.C.</span></div>
    <div class="letter-rule"></div>
    <p class="letter-date">March 12, 2024</p>
    <p class="recipient">Client Name<br>100 Main Street<br>Anytown, MA 01000</p>
    <div class="letter-body">
      <p>Dear Client Name,</p>
      <p>Thank you for contacting our office about your matter. We have reviewed the documents you provided and will outline the next steps below.</p>
      <p>Please keep all records, receipts and correspondence related to this claim. Our team will contact you within the week to schedule a meeting.</p>
      <p>If you have any questions in the meantime, do not hesitate to call us.</p>
    </div>
    <div class="closing">
      <p>Very truly yours,</p>
      <p class="signer">Colvin R. Vandorik</p>
    </div>
    <div class="letter-footer">489 Pellham Avenue, Worcester, Massachusetts 01604 &nbsp;|&nbsp; Phone (508) 555-0142 &nbsp;|&nbsp; www.Vandorik-example.com</div>
  </article>

  <section class="piece envelope-front">
    <div class="brand"><span class="brand-dot"></span><span class="brand-name">VANDORIK LAW, P.C.</span></div>
    <p class="return-address">489 Pellham Avenue<br>Worcester, Massachusetts 01604</p>
    <div class="envelope-band"></div>
  </section>

  <section class="piece envelope-back">
    <svg width="600" height="220" viewBox="0 0 600 220" aria-hidden="true">
      <rect width="600" height="220" fill="#fff"/>
      <path d="M0 0 H600 V30 L300 120 L0 30 Z" fill="#1e3a8c"/>
      <path d="M0 30 L300 120 L600 30" fill="none" stroke="#d5d9e2" stroke-width="1"/>
      <path d="M0 220 L250 110 M600 220 L350 110" stroke="#e3e6ec" stroke-width="1"/>
      <circle cx="300" cy="120" r="14" fill="#fff" stroke="#1e3a8c" stroke-width="2"/>
    </svg>
  </section>

  <section class="piece card card-front">
    <div class="brand"><span class="brand-dot"></span><span class="brand-name">VANDORIK LAW, P.C.</span></div>
    <ul class="contact-list">
      <li>489 Pellham Avenue, Worcester, MA 01604</li>
      <li><b>Phone</b>(508) 555-0142</li>
      <li><b>Fax</b>(508) 555-0143</li>
      <li><b>Email</b>Colvin@Vandorik-example.com</li>
      <li><b>Web</b>www.Vandorik-example.com</li>
    </ul>
    <div class="card-holder">
      <p class="name">Colvin R. Vandorik</p>
      <p class="role">Attorney &amp; Counselor at Law</p>
    </div>
    <div class="card-stripe"></div>
  </section>

  <section class="piece card card-back">
    <div class="brand"><span class="brand-dot"></span><span class="brand-name">VANDORIK LAW, P.C.</span></div>
    <p class="practice-title">Areas of Practice</p>
    <ul class="practice-list">
      <li>Workers' Compensation &nbsp;·&nbsp; Car Accidents</li>
      <li>Personal Injury &nbsp;·&nbsp; Family Law</li>
      <li>Criminal Law</li>
    </ul>
  </section>

</body>
</html>
```